Banner ad for hyper local news site

We need a banner (that we will use on our own site) to explain to people that they can "be the reporter" in their local area. Lanternway is an Australia community news network. We cover local news on a daily basis but also allow people and organisations to publish their own news direct to the site. We are trying to encourage local dialogue and to empower people to talk about the things that matter to them and get their issues on the news agenda.

We need a 'call to action' banner that explains to our users that they can post their own stories on the site.

Some suggested text (thinking this would be rolling)

*Lanternway is YOUR voice in the community
*You can 'be the reporter' and write your own news
*To be heard, contribute your stories, click here - it's free

The banner doesn't have to be slick - we'd prefer a warm and friendly community feeling....but also something in keeping with the look and feel of our site wwww.lanternway-example.com.au

Industry/Entity Type

News

```html
<!DOCTYPE html>
<html lang="en">
<head>
<meta charset="utf-8">
<title>Lanternway – You can 'be the reporter' banner set</title>
<link rel="stylesheet" href="https://fonts.googleapis.com/css2?family=Ubuntu:wght@700&display=swap">
<style>
  :root {
    --page-bg: #9ba797;
    --paper-light: #efe7cf;
    --paper-mid: #e2d6b4;
    --paper-dark: #d3c59d;
    --paper-edge: #8d8f80;
    --ink-green: #23801a;
    --ink-red: #980b0b;
    --ink-olive: #426c14;
    --shadow: rgba(40, 30, 10, 0.55);
  }
  * { box-sizing: border-box; margin: 0; padding: 0; }
  html, body {
    width: 1200px;
    height: 641px;
    overflow: hidden;
    background: var(--page-bg);
  }
  .banner-set {
    position: relative;
    width: 1200px;
    height: 641px;
  }
  .banner {
    position: absolute;
    left: 0;
    width: 1200px;
    height: 140px;
    display: flex;
    align-items: center;
    padding-left: 38px;
    border-top: 3px solid var(--paper-edge);
    border-bottom: 3px solid var(--paper-edge);
    background:
      radial-gradient(ellipse at 30% 40%, rgba(255,255,255,0.35), transparent 60%),
      radial-gradient(ellipse at 80% 70%, rgba(160,140,90,0.25), transparent 55%),
      linear-gradient(180deg, var(--paper-light) 0%, var(--paper-mid) 55%, var(--paper-dark) 100%);
  }
  .banner--green { top: 20px; }
  .banner--red { top: 244px; }
  .banner--olive { top: 458px; }
  .banner__headline {
    font-family: "Ubuntu", "Trebuchet MS", sans-serif;
    font-weight: 700;
    font-size: 96px;
    letter-spacing: -1px;
    white-space: pre;
    line-height: 1;
    text-shadow: 4px 5px 5px var(--shadow);
  }
  .banner--green .banner__headline { color: var(--ink-green); }
  .banner--red .banner__headline { color: var(--ink-red); }
  .banner--olive .banner__headline { color: var(--ink-olive); }
</style>
</head>
<body>
  <main class="banner-set">
    <section class="banner banner--green">
      <h1 class="banner__headline">You can  'be the reporter'</h1>
    </section>
    <section class="banner banner--red">
      <p class="banner__headline">You can  'be the reporter'</p>
    </section>
    <section class="banner banner--olive">
      <p class="banner__headline">You can  'be the reporter'</p>
    </section>
  </main>
</body>
</html>
```